Where's my Gym Buddy? looking to do two promotions as listed in project description

looking for two designs.

1: selfie frame design!! (wording) Copper Stride Festival, my Summer fitness has started, Tag a friend who should be joining me. T.C Tag your posts to @pepperboxsydney to win points for the competition. (Snow graphic) in a selfie frame design. this needs to be the same design but across different departments as seen at the top of the photo's I've attached EG: #pepperboxfitness #pepperboxindoor #pepperboxswim #pepperboxwyong

2: Selfie Frame Design!! (Wording) Where's my gym buddy?, Tag a friend who should be at the gym, T.C.Tag your posts to @pepperboxsydney to win points for the competition. Find Flimbo Feel Selfie frame design

Target Market(s)

Gym Members

Industry/Entity Type

Gym

Colors

Designer to choose colors to be used in the design.

Requirements
Must have
• quirky and funky design, must include wording listed, must be a selfie frame design
Should not have
• whilst we are a big corporate gym, we pride ourselves on having really funky advertisements, so please no boring business corporate typical designs

```html
<!DOCTYPE html>
<html lang="en">
<head>
<meta charset="utf-8">
<title>Where's My Gym Buddy? Selfie Frame</title>
<link rel="stylesheet" href="https://fonts.googleapis.com/css2?family=Cinzel:wght@700;900&family=Lato:wght@900&display=swap">
<style>
  :root {
    --stripe-red: #ec1c24;
    --paper: #ffffff;
    --ink-blue: #2e86b0;
    --ink-red: #e3232b;
    --shadow: rgba(0,0,0,0.35);
  }
  html, body {
    margin: 0;
    padding: 0;
    width: 848px;
    height: 1200px;
    overflow: hidden;
    background: var(--paper);
  }
  .canvas {
    position: relative;
    width: 848px;
    height: 1200px;
    overflow: hidden;
  }
  .artboard {
    position: absolute;
    left: 0;
    top: 0;
    width: 919px;
    height: 1300px;
    transform-origin: 0 0;
    transform: scale(0.92274);
    background: repeating-linear-gradient(
      to bottom,
      var(--stripe-red) 0 38px,
      var(--paper) 38px 76px
    );
    background-position: 0 -4px;
    font-family: "Cinzel", Georgia, serif;
  }
  .title-card {
    position: absolute;
    left: 44px;
    top: 62px;
    width: 832px;
    height: 172px;
    margin: 0;
    box-sizing: border-box;
    background: var(--paper);
    border: 5px solid var(--ink-blue);
    box-shadow: 3px 4px 6px var(--shadow);
    transform: rotate(-1.6deg);
    display: flex;
    align-items: center;
    justify-content: center;
    gap: 14px;
    white-space: nowrap;
  }
  .title-where {
    color: var(--ink-blue);
    font-weight: 900;
    font-size: 104px;
    line-height: 1;
    letter-spacing: -2px;
    font-variant: small-caps;
  }
  .title-buddy {
    display: flex;
    flex-direction: column;
    align-items: center;
    color: var(--ink-red);
    font-weight: 900;
    line-height: 0.9;
    margin-top: -8px;
  }
  .title-buddy .small { font-size: 42px; }
  .title-buddy .big { font-size: 64px; letter-spacing: -1px; }
  .title-mark {
    color: var(--ink-blue);
    font-weight: 900;
    font-size: 96px;
    line-height: 1;
  }
  .selfie-window {
    position: absolute;
    left: 0;
    top: 0;
  }
  .caption {
    position: absolute;
    margin: 0;
    box-sizing: border-box;
    background: var(--paper);
    box-shadow: 3px 4px 6px var(--shadow);
    text-align: center;
    font-weight: 900;
    font-variant: small-caps;
    white-space: nowrap;
  }
  .caption .at {
    font-family: "Lato", Arial, sans-serif;
    font-size: 0.82em;
    font-weight: 900;
  }
  .caption-tag {
    left: 46px;
    top: 1076px;
    width: 826px;
    height: 68px;
    border: 5px solid var(--ink-blue);
    color: var(--ink-red);
    font-size: 36px;
    line-height: 56px;
    transform: rotate(-0.9deg);
  }
  .caption-terms {
    left: 26px;
    top: 1174px;
    width: 866px;
    height: 106px;
    border: 5px solid var(--ink-red);
    color: var(--ink-blue);
    font-size: 37px;
    line-height: 38px;
    padding-top: 11px;
    transform: rotate(0.5deg);
  }
</style>
</head>
<body>
  <main class="canvas">
    <div class="artboard">
      <svg class="selfie-window" width="919" height="1300" viewBox="0 0 919 1300" aria-hidden="true">
        <defs>
          <filter id="window-shadow" x="-10%" y="-10%" width="120%" height="120%">
            <feDropShadow dx="3" dy="4" stdDeviation="4" flood-color="#000" flood-opacity="0.35"/>
          </filter>
          <filter id="inner-shade" x="-10%" y="-10%" width="120%" height="120%">
            <feGaussianBlur stdDeviation="6"/>
          </filter>
        </defs>
        <polygon points="66,302 800,250 852,1010 122,1062" fill="#ffffff" filter="url(#window-shadow)"/>
        <polygon points="77,312 794,261 842,1002 131,1053" fill="none" stroke="#000" stroke-opacity="0.25" stroke-width="6" filter="url(#inner-shade)"/>
        <polygon points="77,312 794,261 842,1002 131,1053" fill="none" stroke="#d8d8d8" stroke-width="1.5"/>
      </svg>

      <header class="title-card">
        <span class="title-where">Where's</span>
        <span class="title-buddy">
          <span class="small">MY GYM</span>
          <span class="big">BUDDY</span>
        </span>
        <span class="title-mark">?</span>
      </header>

      <p class="caption caption-tag">Tag a friend who should be at the gym,</p>
      <p class="caption caption-terms">T.C.Tag your posts to <span class="at">@</span>pepperboxsydney<br>to win points for the competition.</p>
    </div>
  </main>
</body>
</html>
```